依頼詳細
シニア向け通販媒体にて展開するA5サイズ片面カラーのチラシの作成を依頼致します。年配者の女性をターゲットにしていますので、読みやすく、安心感がありかつ雰囲気のあるデザインを期待致します。
記載項目
詳しくは添付の指示書、画像をご確認をお願い申し上げます。
サイズ
A5
ページ数
片面
希望イメージ
• +5 0 +5
• シンプル
複雑
• 単色
カラフル
• 暗い
明るい
• 日常
高級
• 遊び心
厳粛
• 未来的
伝統的
• 女性的
男性的
希望する色
赤系、黄・オレンジ系
納品ファイル
• イラストレーター形式 (.ai)
補足説明
依頼公開後の追記内容
申込書は別紙になりますので、会社名や申し込み方法や電話番号の記載は必要ございません。
パッケージ画像は1袋のみの掲載でお願い申し上げます。
■ 選んだ理由

インパクトがあり雰囲気もよく何より干しいもが美味しそうに見えるので採用させていただきました。

■ 提案者全員のお礼・コメント

皆様、たくさんの素晴らしいご提案をありがとうございます。
どのデザインも素晴らしくとても悩みました。
また機会がございましたらよろしくお願いいたします。

```html
<!DOCTYPE html>
<html lang="ja">
<head>
<meta charset="utf-8">
<title>絶品干しいも チラシ</title>
<link rel="stylesheet" href="https://fonts.googleapis.com/css2?family=Shippori+Mincho+B1:wght@700;800&family=Noto+Sans+JP:wght@400;700;900&display=swap">
<style>
:root{
  --cream:#fbf3e3;
  --brown:#6b3a1c;
  --orange:#e9862a;
  --orange-deep:#d9661d;
  --red:#d9352a;
  --ink:#3a2a1e;
  --white:#ffffff;
  --gold:#f3c568;
}
*{margin:0;padding:0;box-sizing:border-box}
html,body{width:855px;height:1200px;overflow:hidden;background:var(--cream)}
.flyer{position:relative;width:855px;height:1200px;overflow:hidden;background:var(--cream);font-family:"Noto Sans JP",sans-serif;color:var(--ink)}
.flyer p,.flyer h1,.flyer h2,.flyer span{white-space:nowrap}
.floral{position:absolute;left:0;top:0;width:330px;height:160px;background:radial-gradient(circle at 30% 40%,#f2b28a,#f6d8bd 60%,rgba(251,243,227,0) 80%)}
.hero-photo{position:absolute;left:0;top:150px;width:585px;height:560px;border-radius:0 40px 40px 0;background:linear-gradient(135deg,#f9d27a 0%,#eea13a 45%,#d9782a 75%,#f4c870 100%)}
.potato-art{position:absolute;left:715px;top:670px;width:125px;height:165px;border-radius:50%;background:radial-gradient(ellipse,#b34a5c,#d88b7a 60%,rgba(251,243,227,0) 72%)}
.care-label{position:absolute;left:23px;top:18px;font-size:19px;font-weight:700;color:var(--white);letter-spacing:.05em}
.no-additive{position:absolute;left:23px;top:60px;width:240px;height:57px;background:var(--orange);color:var(--white);font-size:31px;font-weight:900;display:flex;align-items:center;justify-content:center}
.tagline{position:absolute;left:518px;top:20px;width:70px;height:580px;background:var(--orange);border-radius:35px;writing-mode:vertical-rl;display:flex;align-items:center;justify-content:center;color:var(--white);font-family:"Shippori Mincho B1",serif;font-weight:800;font-size:34px;letter-spacing:.08em}
.tagline::before,.tagline::after{content:"";width:12px;height:12px;border-radius:50%;background:var(--white);margin:14px 0}
.title-top{position:absolute;left:602px;top:30px;font-family:"Shippori Mincho B1",serif;font-weight:800;font-size:120px;line-height:1;color:var(--brown)}
.title-main{position:absolute;left:700px;top:170px;writing-mode:vertical-rl;font-family:"Shippori Mincho B1",serif;font-weight:800;font-size:120px;line-height:1;color:var(--brown)}
.origin{position:absolute;left:610px;top:185px;writing-mode:vertical-rl;font-size:28px;line-height:1;font-weight:700;color:var(--orange-deep)}
.story{position:absolute;left:40px;top:728px;font-size:19px;line-height:1.7;font-weight:700;color:var(--ink)}
.volume{position:absolute;left:508px;top:842px;display:flex;align-items:center;gap:8px;white-space:nowrap}
.volume .tag{background:var(--orange-deep);color:var(--white);font-size:20px;font-weight:900;padding:3px 10px;border-radius:8px}
.volume .amount{font-size:28px;font-weight:900;color:var(--orange-deep);line-height:1}
.volume .amount b{font-size:54px}
.offer{position:absolute;left:28px;top:915px;width:798px;height:270px;background:var(--white);border:2px solid var(--gold);border-radius:6px}
.pack-photo{position:absolute;left:12px;top:14px;width:170px;height:238px;border-radius:14px;background:linear-gradient(160deg,#f4ebe0,#e9b46b 55%,#d9862f)}
.product-name{position:absolute;left:200px;top:16px;width:580px;text-align:center;font-size:28px;font-weight:700;padding-bottom:10px;border-bottom:2px solid var(--gold)}
.price-row{position:absolute;left:200px;display:flex;align-items:baseline;gap:12px;font-weight:700;white-space:nowrap}
.price-row .label{font-size:18px;color:var(--white);padding:3px 10px}
.regular{top:82px}
.regular .label{background:var(--orange)}
.regular .yen{font-size:44px;color:var(--ink);line-height:1.1}
.bundle{top:150px}
.bundle .label{background:var(--red)}
.bundle .yen{font-size:44px;color:var(--red);line-height:1.1}
.yen small{font-size:20px}
.tax{font-size:20px;color:var(--ink)}
.details{position:absolute;left:200px;top:222px;font-size:19px;color:var(--ink)}
</style>
</head>
<body>
<div class="flyer">
  <div class="floral" role="img" aria-label="淡い色の花の飾り"></div>
  <div class="hero-photo" role="img" aria-label="黄金色の干しいもを積み重ねた写真"></div>
  <div class="potato-art" role="img" aria-label="さつまいものイラスト"></div>

  <p class="care-label">安心へのこだわり</p>
  <p class="no-additive">無添加・無着色</p>

  <p class="tagline">驚きの甘さとやわらかさ</p>
  <h1><span class="title-top">絶品</span><span class="title-main">干しいも</span></h1>
  <p class="origin">茨城県産「紅はるか」使用</p>

  <p class="story">「紅はるか」は蜜芋とよばれるほど<br>糖度が高く、まらかい食感が特徴です。<br>もう他の干しいもは食べられなくなるほど<br>美味しい「やわらか干しいも」を<br>是非この機会にお試しください！</p>

  <div class="volume"><span class="tag">内容量</span><span class="amount">たっぷり<b>200</b>g</span></div>

  <section class="offer">
    <div class="pack-photo" role="img" aria-label="干しいも商品パッケージの写真"></div>
    <h2 class="product-name">やわらか干しいも雅 200g / 1袋</h2>
    <div class="price-row regular"><span class="label">本体価格</span><span class="yen">978<small>円</small></span><span class="tax">（税込 1,056円）</span></div>
    <div class="price-row bundle"><span class="label">お買い得2袋パック</span><span class="yen">1,856<small>円</small></span><span class="tax">（税込 2,004円）</span></div>
    <p class="details">原材料：さつまいも（茨城県産）　賞味期限：45日</p>
  </section>
</div>
</body>
</html>
```